http://www.brindlevane.com/ New Ecommerce Site

We are redesigning Brindlevane.com on shopquarry.com.

We need to get a design for the ecommerce site.

They have about 15-45 products and these are the menu items that they need on the pages.

Knives:
Kitchen Knives
Neck Knives
Outdoor Knives
Graywillow Knives
Clearance Knives
Premium Knives
Misc. Product:
Waterstones
Books
DVDs
T-Shirts
Scissors
Bladesmithing School
Videos
Links
Testimonials/Feedback
Contact Tobias Form
Knife Care and Maintenance Tips
Knife Sharpening
Knife Archives
Kitchen Knife Archives

We need several pages designed.

- Category Page
- Single Item page
- Knive Archive Pages (This is where old knives are stored that are not being sold anymore)
- Featured Product pages.
- Information pages
- checkout

The design has to be VERY elagant, like veltrane.com.
And it has to be very easy to navigate and buy items like http://bladesmovequick.com/

Thanks,
Peter Ostrander

Requirements
Must have
• Must be very elegant, and have the menu items somewhere on the pages.

```html
<!DOCTYPE html>
<html lang="en">
<head>
<meta charset="utf-8">
<title>Brindlevane Cutlery</title>
<link href="https://fonts.googleapis.com/css2?family=Cinzel:wght@400&family=Tinos:ital,wght@0,400;0,700;1,400&family=Open+Sans:wght@400;600&display=swap" rel="stylesheet">
<style>
:root{
  --brown-dark:#34261f;
  --brown-panel:#3a2d27;
  --red:#c3112c;
  --red-dark:#8f0b1f;
  --ink:#333;
  --muted:#777;
  --line:#e2e2e2;
  --footer:#ededed;
  --base:#2b2b2b;
  --wood-a:#8a5f3c;
  --wood-b:#4a2f1d;
}
*{box-sizing:border-box;margin:0;padding:0}
html,body{width:711px;height:1200px;overflow:hidden}
body{position:relative;background:#fff;font-family:"Tinos",serif;color:var(--ink)}
.abs{position:absolute}
a{color:inherit;text-decoration:none}

/* header */
.site-header{left:0;top:0;width:711px;height:106px;background:var(--brown-dark)}
.logo{left:79px;top:14px;font-family:"Cinzel",serif;font-size:27px;line-height:25px;color:#d9d2cc;letter-spacing:1px}
.tagline{left:81px;top:79px;font-size:9px;color:#cfc5bd;letter-spacing:.3px}
.top-links{left:371px;top:30px;font-family:"Open Sans",sans-serif;font-size:6.5px;color:#e6ddd6;display:flex;gap:6px;align-items:center;text-transform:uppercase}
.top-links .sep{color:#a99}
.search{left:517px;top:65px;width:117px;height:19px;background:#fff;border-radius:2px;font-size:7px;font-style:italic;color:#aaa;padding:5px 9px}
.search svg{position:absolute;right:5px;top:4px}

/* nav */
.main-nav{left:0;top:106px;width:711px;height:32px;background:linear-gradient(#fff,#f1f1f1);border-bottom:1px solid #ddd}
.main-nav a{position:absolute;top:11px;font-size:8.5px;text-transform:uppercase;color:#222}
.main-nav .div{position:absolute;top:0;width:1px;height:32px;background:#ddd}

/* hero */
.hero{left:0;top:138px;width:711px;height:280px;background:linear-gradient(100deg,var(--wood-b) 0%,var(--wood-a) 45%,#6d4a2e 75%,#3d281a 100%)}
.hero-copy{left:77px;top:183px;width:218px;height:184px;background:rgba(40,34,30,.78);color:#fff;padding:9px 12px}
.hero-copy h1{font-weight:400;font-size:27px;line-height:28px;white-space:nowrap}
.hero-copy h2{font-weight:400;font-size:18px;line-height:22px;margin:0 0 9px 5px;white-space:nowrap}
.hero-copy p{font-size:7.4px;line-height:9.4px;margin-bottom:8px;color:#eee}
.btn{display:inline-block;background:var(--red);color:#fff;font-family:"Tinos",serif;font-size:7px;text-transform:uppercase;box-shadow:0 2px 0 var(--red-dark);text-align:center}
.read-more{left:214px;top:339px;width:67px;height:17px;line-height:17px}
.dots{left:86px;top:399px;display:flex;gap:3px}
.dots span{width:8px;height:8px;border-radius:50%;background:#111}
.dots span:first-child{background:#fff}

/* sidebar */
.box{border:1px solid var(--line);background:#fff}
.categories{left:77px;top:437px;width:130px;height:263px}
.box-title{font-size:12px;padding:5px 13px;border-bottom:1px solid var(--line);height:24px}
.cat-list{list-style:none;font-size:8px;margin-left:14px;color:var(--ink)}
.cat-list li{height:15px;display:flex;align-items:center;gap:8px;color:var(--ink)}
.cat-list .arrow{font-family:"Open Sans",sans-serif;font-size:8px;color:#555}
.cat-group{font-size:9px;font-weight:700;margin:6px 0 2px 14px;display:flex;gap:6px;align-items:center}
.care{left:77px;top:716px;width:130px;height:146px;background:var(--brown-panel);color:#fff;padding:8px 12px}
.care h3{font-weight:400;font-size:11.5px;margin-bottom:6px}
.care p{font-size:6.5px;font-style:italic;line-height:10px;margin-bottom:6px}
.field{width:106px;height:18px;background:#fff;color:#999;font-size:7.5px;font-style:italic;padding:4px 8px;margin-bottom:7px}
.subscribe{width:67px;height:17px;line-height:17px;margin-left:39px;font-weight:700}
.news{left:77px;top:878px;width:130px;height:109px;padding:0 10px;overflow:hidden}
.news h3{font-weight:400;font-size:11.5px;color:var(--red);padding:6px 0 5px;border-bottom:1px solid var(--line);display:flex;justify-content:space-between;line-height:13px}
.news-item{font-family:"Open Sans",sans-serif;padding:5px 2px 4px;border-bottom:1px solid var(--line)}
.news-item:last-child{border:0}
.news-item b{display:block;font-size:6.5px;line-height:9px;font-weight:400;color:#222;margin-bottom:1px}
.news-item span{display:block;font-size:6px;color:#888;line-height:9.5px}

/* products */
.featured-head{left:219px;top:437px;width:415px;height:24px;padding:5px 10px;font-size:12px;color:var(--red);display:flex;justify-content:space-between}
.chev{color:var(--red);font-family:"Open Sans",sans-serif;font-weight:600;letter-spacing:3px}
.card-img{width:131px;height:88px}
.product-name{font-size:10.5px;text-align:center;width:131px}
.price{font-size:11px}
.cart{width:59px;height:16px;line-height:16px;font-family:"Open Sans",sans-serif;font-weight:600;font-size:6.5px}
.misc{left:219px;top:799px;width:415px;height:171px}
.misc .box-title{padding-left:18px}
.misc-img{width:112px;height:79px}
.side-arrow{font-size:16px;color:#555;font-family:"Open Sans",sans-serif}

/* footer */
.site-footer{left:0;top:1013px;width:711px;height:121px;background:var(--footer);font-family:"Open Sans",sans-serif}
.foot-col h4{font-size:8px;font-weight:400;color:#444;margin-bottom:6px}
.foot-col li{list-style:none;font-size:6.7px;color:#888;height:15px}
.foot-input{left:518px;top:1057px;width:116px;height:17px;background:#bbb;border-radius:2px}
.social{top:1094px;width:16px;height:16px;border-radius:50%;background:#aaa}
.base{left:0;top:1134px;width:711px;height:66px;background:var(--base);color:#ddd}
.copy{font-size:7.5px;line-height:11px}
.pay{font-size:11px}
.cards{display:flex;gap:2px}
.cards span{width:20px;height:12px;background:#f2f2f2;border-radius:1px}
</style>
</head>
<body>

<header class="abs site-header">
  <div class="abs logo">BRINDLEVANE<br>CUTLERY</div>
  <div class="abs tagline">17th Generation Kuroyama Bladesmith</div>
  <nav class="abs top-links">
    <a>Sign In</a><span class="sep">|</span><a>My Account</a><span class="sep">|</span>
    <svg width="10" height="8" viewBox="0 0 10 8"><path d="M1 2h8l-1 6H2z" fill="#e6ddd6"/><path d="M3 2a2 2 0 0 1 4 0" stroke="#e6ddd6" fill="none"/></svg>
    <a>Shopping Bag</a><span class="sep">|</span><a>My Wishlist</a><span class="sep">|</span><a>Join Us</a>
  </nav>
  <div class="abs search">Search here...
    <svg width="12" height="11" viewBox="0 0 12 11"><circle cx="4.5" cy="4.5" r="3.3" stroke="#222" stroke-width="1.6" fill="none"/><path d="M7 7l4 3.5" stroke="#222" stroke-width="2"/></svg>
  </div>
</header>

<nav class="abs main-nav">
  <a style="left:78px">Home</a><span class="div" style="left:120px"></span>
  <a style="left:137px">About Us</a><span class="div" style="left:199px"></span>
  <a style="left:215px">Sharpening Videos</a><span class="div" style="left:317px"></span>
  <a style="left:336px">Knives</a><span class="div" style="left:384px"></span>
  <a style="left:398px">Tools</a><span class="div" style="left:440px"></span>
  <a style="left:455px">Instruction</a><span class="div" style="left:525px"></span>
  <a style="left:541px">FAQ</a><span class="div" style="left:575px"></span>
  <a style="left:592px">Contact</a>
</nav>

<section class="abs hero" role="img" aria-label="Photo of a chef's knife resting on a wooden cutting board"></section>
<div class="abs hero-copy">
  <h1>Welcome</h1>
  <h2>to Brindlevane Cutlery</h2>
  <p>Welcome to Brindlevane Cutlery, your source of high performance hand-forged cutlery and world renowned sharpening instruction!</p>
  <p>I am Tobias Brindle, 17th Generation Kuroyama Bladesmith and Certified Master Bladesmith. You will benefit from my 23 years of unique knife making experience.</p>
</div>
<a class="abs btn read-more">Read More</a>
<div class="abs dots"><span></span><span></span><span></span><span></span></div>

<aside class="abs box categories">
  <div class="box-title">Categories</div>
  <ul class="cat-list" style="margin-top:6px">
    <li><span class="arrow">→</span>Kitchen Knives</li>
    <li><span class="arrow">→</span>Neck Knives</li>
    <li><span class="arrow">→</span>Outdoor Knives</li>
    <li><span class="arrow">→</span>Graywillow Knives</li>
    <li><span class="arrow">→</span>Clearance Knives</li>
    <li><span class="arrow">→</span>Premium Knives</li>
  </ul>
  <div class="cat-group"><svg width="9" height="9" viewBox="0 0 9 9"><circle cx="4.5" cy="4.5" r="4" stroke="#555" fill="none"/><path d="M2.5 4.5h4" stroke="#555"/></svg>Misc. Product:</div>
  <ul class="cat-list">
    <li><span class="arrow">→</span>Waterstones</li>
    <li><span class="arrow">→</span>Books</li>
    <li><span class="arrow">→</span>DVDs</li>
    <li><span class="arrow">→</span>T-Shirts</li>
    <li><span class="arrow">→</span>Scissors</li>
    <li><span class="arrow">→</span>Bladesmithing School</li>
    <li><span class="arrow">→</span>Videos</li>
  </ul>
</aside>

<aside class="abs care">
  <h3>Free Knife Care Tips</h3>
  <p>Subscribe for Tobias's Free Knife Care and Maintenance Tips:</p>
  <div class="field">Enter Email..</div>
  <div class="field">Password</div>
  <a class="btn subscribe">Subscribe</a>
</aside>

<aside class="abs box news">
  <h3>News &amp; Events <span class="chev" style="font-size:9px">‹›</span></h3>
  <div class="news-item"><b>AUGUST 1st</b><span>Sed ut perspiciatis unde omnis iste natus error sit volupt</span></div>
  <div class="news-item"><b>AUGUST 1st</b><span>Sed ut perspiciatis unde omnis iste natus error sit volupt</span></div>
</aside>

<div class="abs box featured-head">Featured Products <span class="chev">‹›</span></div>

<div class="abs card-img" style="left:219px;top:473px;background:linear-gradient(135deg,#f4f4f4,#8a8e94)" role="img" aria-label="Photo of kitchen knives"></div>
<div class="abs card-img" style="left:361px;top:473px;background:linear-gradient(90deg,#f3f3f3,#7a3b2a 40%,#c9ccd0 60%,#f3f3f3)" role="img" aria-label="Photo of a neck knife"></div>
<div class="abs card-img" style="left:503px;top:473px;background:linear-gradient(135deg,#f5f5f5,#a9adb3 50%,#7a5530 75%,#f5f5f5)" role="img" aria-label="Photo of a folding outdoor knife"></div>
<div class="abs product-name" style="left:219px;top:567px">Kitchen Knives</div>
<div class="abs product-name" style="left:361px;top:566px">Neck Knives</div>
<div class="abs product-name" style="left:503px;top:567px">Outdoor Knives</div>
<div class="abs price" style="left:221px;top:589px">$80.00</div>
<a class="abs btn cart" style="left:290px;top:590px">Add to Cart</a>
<div class="abs price" style="left:363px;top:588px">$80.00</div>
<a class="abs btn cart" style="left:432px;top:589px">Add to Cart</a>
<div class="abs price" style="left:505px;top:589px">$80.00</div>
<a class="abs btn cart" style="left:575px;top:590px">Add to Cart</a>

<div class="abs card-img" style="left:219px;top:624px;background:linear-gradient(135deg,#c79a5e,#3a3a3a 50%,#b88c55)" role="img" aria-label="Photo of a clearance knife on bamboo"></div>
<div class="abs card-img" style="left:361px;top:624px;background:linear-gradient(135deg,#f5f5f5,#6a2a1f 35%,#c9ccd0 60%,#f5f5f5)" role="img" aria-label="Photo of a premium hunting knife"></div>
<div class="abs card-img" style="left:503px;top:624px;background:linear-gradient(135deg,#e8e2d6,#c99a52 55%,#a4773b)" role="img" aria-label="Photo of a bread knife with sliced bread"></div>
<div class="abs product-name" style="left:219px;top:719px">Clearance Knives</div>
<div class="abs product-name" style="left:361px;top:719px">Premium Knives</div>
<div class="abs product-name" style="left:503px;top:719px">Graywillow Knives</div>
<div class="abs price" style="left:221px;top:742px">$80.00</div>
<a class="abs btn cart" style="left:290px;top:742px">Add to Cart</a>
<div class="abs price" style="left:363px;top:741px">$80.00</div>
<a class="abs btn cart" style="left:432px;top:742px">Add to Cart</a>
<div class="abs price" style="left:505px;top:741px">$80.00</div>
<a class="abs btn cart" style="left:575px;top:742px">Add to Cart</a>

<section class="abs box misc"><div class="box-title">Misc Product</div></section>
<span class="abs side-arrow" style="left:226px;top:867px">‹</span>
<span class="abs side-arrow" style="left:618px;top:867px">›</span>
<div class="abs misc-img" style="left:247px;top:835px;background:linear-gradient(135deg,#f4f4f4,#9cc94a 45%,#d46a2d 80%)" role="img" aria-label="Photo of a stack of books"></div>
<div class="abs misc-img" style="left:372px;top:835px;background:linear-gradient(135deg,#3e7fc1,#1e5a9c 60%,#0e3d70)" role="img" aria-label="Photo of scissors on blue background"></div>
<div class="abs misc-img" style="left:497px;top:835px;background:linear-gradient(135deg,#f6f6f6,#dcdcdc)" role="img" aria-label="Photo of a DVD case and disc"></div>
<div class="abs product-name" style="left:237px;top:922px">Books</div>
<div class="abs product-name" style="left:362px;top:921px">Scissors</div>
<div class="abs product-name" style="left:487px;top:922px">DVDs</div>
<div class="abs price" style="left:249px;top:944px">$20.00</div>
<a class="abs btn cart" style="left:301px;top:941px">Add to Cart</a>
<div class="abs price" style="left:374px;top:942px">$10.00</div>
<a class="abs btn cart" style="left:423px;top:940px">Add to Cart</a>
<div class="abs price" style="left:500px;top:942px">$25.00</div>
<a class="abs btn cart" style="left:548px;top:940px">Add to Cart</a>

<footer class="abs site-footer">
  <div class="abs foot-col" style="left:78px;top:19px"><h4>Customer Services</h4><ul><li>Shopping Guide</li><li>Contact Us</li><li>FAQ</li><li>Track My Order</li><li>Return Policy</li></ul></div>
  <div class="abs foot-col" style="left:192px;top:20px"><h4>My Account</h4><ul><li>Sign in | Register</li><li>Order history</li><li>Message</li><li>Points &amp; Coupons, Gifts</li><li>RMA Request</li></ul></div>
  <div class="abs foot-col" style="left:309px;top:20px"><h4>Company Info</h4><ul><li>Legal window</li><li>About Us</li><li>Why buy from us</li><li>Security &amp; Privacy</li><li>Terms of Use</li></ul></div>
  <div class="abs foot-col" style="left:411px;top:20px"><h4>Partner Program</h4><ul><li>Wholesale</li><li>Affiliated Program</li><li>Partner links</li><li>Drop-shipping</li></ul></div>
  <div class="abs foot-col" style="left:519px;top:19px"><h4>Newsletter</h4></div>
</footer>
<div class="abs foot-input"><svg class="abs" style="right:6px;top:4px" width="9" height="9" viewBox="0 0 9 9"><path d="M1 1l3 3.5L1 8M5 1l3 3.5L5 8" stroke="#333" stroke-width="1.4" fill="none"/></svg></div>
<span class="abs social" style="left:517px"></span>
<span class="abs social" style="left:537px"></span>
<span class="abs social" style="left:556px"></span>
<span class="abs social" style="left:576px"></span>

<div class="abs base">
  <div class="abs copy" style="left:79px;top:18px">© 2013. BV. All Rights Reserved<br>Privacy Policy.</div>
  <div class="abs pay" style="left:586px;top:13px">Pay From</div>
  <div class="abs cards" style="left:522px;top:37px"><span></span><span></span><span></span><span></span><span style="width:30px"></span></div>
</div>

</body>
</html>
```